Tiny educational app company needs a big new website

We need to re-do our ageing website (www.brightpebblesoft.com). Our site is mostly visited by primary school teachers or parents of primary school kids. 90% of our apps are iPad only so an iPad optimised design would be helpful.

We would like the monkey to remain part of the design if possible. I'm not sure if the orange/ blue/ white should stay - if you have a good design and a strong opinion it should go we could be open to change.

Target Market(s)

Teachers, parents

Industry/Entity Type

Education

Number of Pages Required

3 page

Font styles to use
Sans Serif

Colors

Designer to choose colors to be used in the design.

Requirements
Must have
• Needs to show all of our apps (somehow... open to a new way of achieving this)

```html
<!DOCTYPE html>
<html lang="en">
<head>
<meta charset="utf-8">
<title>Bright Pebble Soft – Apps</title>
<link rel="stylesheet" href="https://fonts.googleapis.com/css2?family=Montserrat:wght@800&family=Poppins:ital,wght@1,300;1,400&display=swap">
<style>
  :root {
    --orange-bg: #e0894c;
    --band-blue: #1d4f72;
    --footer-dark: #212227;
    --heading-orange: #d85a26;
    --link-gold: #e8a94a;
    --muted-grey: #8b8b91;
    --icon-navy: #1f4e6e;
    --icon-orange: #d6611f;
    --icon-white: #f7f7f4;
  }
  * { margin: 0; padding: 0; box-sizing: border-box; }
  html, body { width: 1200px; height: 1200px; overflow: hidden; }
  body { position: relative; background: var(--footer-dark); font-family: "Poppins", sans-serif; }

  .app-showcase { position: absolute; left: 0; top: 0; width: 1200px; height: 464px; background: var(--orange-bg); overflow: hidden; }
  .app-icon { position: absolute; width: 207px; height: 207px; border-radius: 34px; }
  .app-icon--navy { background: linear-gradient(160deg, var(--icon-navy) 0%, #2a5f82 60%, var(--icon-orange) 100%); }
  .app-icon--light { background: linear-gradient(160deg, var(--icon-white) 0%, #f1e3cf 70%, var(--icon-orange) 100%); }
  .app-icon--square { border-radius: 0; }

  .accent-band { position: absolute; left: 0; top: 464px; width: 1200px; height: 19px; background: var(--band-blue); }

  .footer-heading { position: absolute; font-family: "Montserrat", sans-serif; font-weight: 800; font-size: 31px; letter-spacing: 1.5px; color: var(--heading-orange); line-height: 1; }
  .link-list { position: absolute; list-style: none; font-style: italic; font-weight: 400; color: var(--link-gold); text-transform: uppercase; white-space: nowrap; }
  .link-list--apps { left: 45px; top: 586px; font-size: 23px; line-height: 28.8px; letter-spacing: 5px; font-weight: 300; }
  .link-list--social { left: 530px; top: 579px; font-size: 22px; line-height: 57.6px; letter-spacing: 1.5px; }
  .link-list--main { left: 800px; top: 573px; font-size: 22px; line-height: 57.6px; letter-spacing: 1.5px; }
  .link-list--curriculum { left: 581px; top: 1021px; font-size: 22px; line-height: 28.8px; letter-spacing: 1.5px; }
  .copyright { position: absolute; left: 47px; top: 1110px; font-style: italic; font-weight: 300; font-size: 26px; letter-spacing: 1.5px; color: var(--muted-grey); text-transform: uppercase; }
</style>
</head>
<body>
  <section class="app-showcase">
    <div class="app-icon app-icon--navy" style="left:46px; top:-75px;" role="img" aria-label="Dot Tile Adding app icon"></div>
    <div class="app-icon app-icon--navy" style="left:308px; top:-75px;" role="img" aria-label="Blocks: Adding app icon"></div>
    <div class="app-icon app-icon--navy" style="left:647px; top:-75px;" role="img" aria-label="Blocks: Taking Away app icon"></div>
    <div class="app-icon app-icon--navy app-icon--square" style="left:947px; top:-75px;" role="img" aria-label="Times Grid app icon"></div>

    <div class="app-icon app-icon--light app-icon--square" style="left:47px; top:199px;" role="img" aria-label="Graph Builder app icon"></div>
    <div class="app-icon app-icon--navy app-icon--square" style="left:308px; top:199px;" role="img" aria-label="Quick Dot Cards app icon"></div>
    <div class="app-icon app-icon--light" style="left:646px; top:199px;" role="img" aria-label="Number Words app icon"></div>
    <div class="app-icon app-icon--navy" style="left:947px; top:199px;" role="img" aria-label="Pairs to Ten app icon"></div>
  </section>

  <div class="accent-band"></div>

  <footer>
    <h2 class="footer-heading" style="left:124px; top:527px;">APPS</h2>
    <ul class="link-list link-list--apps">
      <li>Dot Tile Adding</li>
      <li>Pairs to Ten</li>
      <li>Times Grid</li>
      <li>Number Paths</li>
      <li>Place Value Blocks</li>
      <li>Blocks: Adding</li>
      <li>Blocks: Taking Away</li>
      <li>Quick Dot Cards</li>
      <li>Beetle Counting</li>
      <li>Graph Builder</li>
      <li>Gap Numbers</li>
      <li>Fraction Stack</li>
      <li>Grid Points</li>
      <li>Secret Number</li>
      <li>Coin Counter</li>
      <li>Number Words</li>
    </ul>

    <h2 class="footer-heading" style="left:516px; top:527px;">SOCIAL</h2>
    <ul class="link-list link-list--social">
      <li>Chatterly</li>
      <li>Pinspire</li>
      <li>Blog</li>
      <li>ClipCast</li>
      <li>IdeaBox</li>
      <li>FriendPage</li>
    </ul>

    <h2 class="footer-heading" style="left:800px; top:527px;">MAIN</h2>
    <ul class="link-list link-list--main">
      <li>Home</li>
      <li>Support</li>
      <li>Cookie Policy</li>
      <li>Volume Purchasing</li>
      <li>App Privacy</li>
    </ul>

    <h2 class="footer-heading" style="left:623px; top:966px;">CURRICULUM</h2>
    <ul class="link-list link-list--curriculum">
      <li>Australian Curriculum</li>
      <li>US Common Core State Standards</li>
      <li>UK School Curriculum</li>
      <li>New Zealand Curriculum</li>
    </ul>

    <p class="copyright">© Bright Pebble Soft 2016</p>
  </footer>
</body>
</html>
```